7 M.E.R. Dawn (Praise by Lamp) EP Project "Walk Along Home"

We need a digital design image for music downloads
Updates

7 M.E.R. dawn (Praise By Lamp) is the group name and Walk Along Home is the title of the project

Target Market(s)

Christian Community

Industry/Entity Type

Digital

Requirements
Nice to have
• Included something with a cross would be nice

```html
<!DOCTYPE html>
<html lang="en">
<head>
<meta charset="utf-8">
<title>Walk Along Home — 7 M.E.R. Dawn</title>
<link rel="stylesheet" href="https://fonts.googleapis.com/css2?family=Inter:wght@300&display=swap">
<style>
  :root {
    --page-bg: #ffffff;
    --shadow-deep: #0e0a04;
    --bark-brown: #2a1d08;
    --moss-olive: #4a3a0e;
    --amber-light: #c98a1c;
    --sun-gold: #f6d160;
    --sun-core: #fff6d2;
    --title-white: #ffffff;
    --cross-tint: rgba(20, 14, 4, 0.28);
    --cross-edge: rgba(255, 220, 140, 0.12);
  }
  * { margin: 0; padding: 0; box-sizing: border-box; }
  html, body {
    width: 1200px;
    height: 900px;
    overflow: hidden;
    background: var(--page-bg);
  }
  .cover {
    position: absolute;
    left: 209px;
    top: 66px;
    width: 778px;
    height: 777px;
    overflow: hidden;
  }
  .cover-scene {
    position: absolute;
    inset: 0;
    background:
      radial-gradient(circle at 92% 2%, var(--sun-core) 0%, var(--sun-gold) 8%, rgba(246, 209, 96, 0) 34%),
      radial-gradient(ellipse at 95% 70%, rgba(214, 160, 40, 0.85) 0%, rgba(214, 160, 40, 0) 45%),
      radial-gradient(ellipse at 85% 95%, rgba(190, 170, 50, 0.9) 0%, rgba(190, 170, 50, 0) 40%),
      linear-gradient(115deg, var(--shadow-deep) 0%, var(--bark-brown) 35%, var(--moss-olive) 60%, var(--amber-light) 100%);
  }
  .cover-cross {
    position: absolute;
    inset: 0;
  }
  .cover-title {
    position: absolute;
    left: 17px;
    bottom: 22px;
    font-family: "Inter", "Helvetica Neue", Arial, sans-serif;
    font-weight: 300;
    font-size: 50px;
    letter-spacing: -0.5px;
    line-height: 1;
    color: var(--title-white);
  }
</style>
</head>
<body>
  <main class="cover">
    <div class="cover-scene" role="img" aria-label="Misty forest river at sunrise with golden light rays through the leaves"></div>
    <svg class="cover-cross" width="778" height="777" viewBox="0 0 778 777" aria-hidden="true">
      <path d="M361 84 H424 V232 H559 V292 H424 V656 H361 V292 H211 V232 H361 Z"
            fill="var(--cross-tint)" stroke="var(--cross-edge)" stroke-width="1.5"/>
    </svg>
    <h1 class="cover-title">Walk Along Home</h1>
  </main>
</body>
</html>
```